Sale of South Sea and Tahitian Pearl Jewellery, online business

I need a business card designed for my website business. We sell South Sea and Tahitian Pearl Jewellery. The colour theme for the website is black and white and would like to carry this through to business cards. Our brand is very elegant and stylish, would like sketch picture of women or fashion involving pearls if not the sketched picture then have the card very plan. below are pictures of the ideas I like and also the logo and writing that is used on my jewellery boxes.
Font is English Hand DB

Target Market(s)

30 and over women in the high end of the market

Industry/Entity Type

Business

Contact Information for Business Card

Business name - Varno Gems( front of card)
Back of card -Details
Corinne Mabbutt
Gemmologist FGAA
email: corinne@varnogems.com.au
website: varnogems.com.au
mob: +61 427 806 193
Perth Australia

Varno Orbix PTY T/AS Varno Gems
ABN 72 384 516 907

Colors
1b1b1b
ffffff
85cae6

Requirements
Must have
• Black and white colour preferably black card with white writing and picture.
• The Same writing as logo and writing on box packaging, attached a file with writing.
• Business name on one side of the card and all other details on the other side.
• Can have tiny hints of the tiffany blue colour.
• Font: English Hand DB
Nice to have
• I really like the idea of having a sketch of a stylish or elegent lady wearing pearls or a sketch of a pearl, if not the sketch a really plain and simple card.
Should not have
• busy patterns.

```html
<!DOCTYPE html>
<html lang="en">
<head>
<meta charset="utf-8">
<title>Varno Gems – Business Cards</title>
<link rel="stylesheet" href="https://fonts.googleapis.com/css2?family=Pinyon+Script&family=Michroma&family=Arimo:wght@400&display=swap">
<style>
  :root {
    --backdrop: #ececec;
    --card: #1b1b1b;
    --ink: #ffffff;
    --tiffany: #85cae6;
    --ghost: #303030;
    --shadow: rgba(0, 0, 0, 0.28);
  }
  * { margin: 0; padding: 0; box-sizing: border-box; }
  html, body {
    width: 1200px; height: 848px; overflow: hidden;
    background: var(--backdrop);
  }
  .stage { position: relative; width: 1200px; height: 848px; }

  .card {
    position: absolute;
    width: 520px; height: 297px;
    background: var(--card);
    color: var(--ink);
    box-shadow: 0 14px 28px var(--shadow);
    overflow: hidden;
  }
  .card--front { left: 150px; top: 110px; }
  .card--back  { left: 530px; top: 440px; }

  /* Front */
  .brand {
    position: absolute; left: 70px; top: 106px;
    display: flex; align-items: center; gap: 22px;
  }
  .brand__ring {
    width: 82px; height: 82px; border-radius: 50%;
    border: 1.5px solid var(--ink);
    flex: none;
  }
  .brand__name {
    font-family: "Pinyon Script", cursive;
    font-size: 52px; line-height: 1;
    color: var(--ink);
    white-space: nowrap;
  }
  .front__web {
    position: absolute; left: 0; right: 0; bottom: 34px;
    text-align: center;
    font-family: "Michroma", sans-serif;
    font-size: 11px; letter-spacing: 2px;
    color: var(--tiffany);
  }

  /* Back */
  .legal {
    position: absolute; right: 22px; top: 18px;
    text-align: right;
    font-family: "Arimo", sans-serif;
    font-size: 9px; line-height: 1.35;
  }
  .watermark {
    position: absolute; right: 26px; top: 48px;
    text-align: right;
    font-family: "Pinyon Script", cursive;
    font-size: 50px; line-height: 0.95;
    color: var(--ghost);
    white-space: nowrap;
  }
  .person { position: absolute; left: 30px; top: 118px; }
  .person__name {
    font-family: "Pinyon Script", cursive;
    font-size: 44px; line-height: 1;
    font-weight: 400;
    white-space: nowrap;
  }
  .person__line {
    margin-top: 6px;
    display: flex; gap: 16px;
    font-family: "Michroma", sans-serif;
    font-size: 10.5px; letter-spacing: 1.2px;
    white-space: nowrap;
  }
  .person__title { color: var(--tiffany); }
  .person__web { color: var(--ink); }

  .contacts {
    position: absolute; left: 30px; bottom: 24px;
    list-style: none;
  }
  .contacts__item {
    display: flex; align-items: center; gap: 8px;
    font-family: "Michroma", sans-serif;
    font-size: 11px; letter-spacing: 1.2px;
    line-height: 1;
    margin-top: 6px;
  }
  .contacts__icon {
    width: 13px; height: 13px; flex: none;
    background: var(--tiffany); border-radius: 2px;
    display: block;
  }
</style>
</head>
<body>
<main class="stage">

  <section class="card card--front" aria-label="Card front">
    <div class="brand">
      <span class="brand__ring"></span>
      <span class="brand__name">Varno Gems</span>
    </div>
    <p class="front__web">WWW.VARNOGEMS.COM.AU</p>
  </section>

  <section class="card card--back" aria-label="Card back">
    <span class="watermark" aria-hidden="true">Varno<br>Gems</span>
    <p class="legal">Varno Orbix PTY T/AS Varno Gems<br>ABN 72 384 516 907</p>

    <div class="person">
      <h1 class="person__name">Corinne Mabbutt</h1>
      <p class="person__line">
        <span class="person__title">GEMMOLOGIST FGAA</span>
        <span class="person__web">VARNOGEMS.COM.AU</span>
      </p>
    </div>

    <ul class="contacts">
      <li class="contacts__item">
        <svg class="contacts__icon" viewBox="0 0 13 13" aria-hidden="true">
          <circle cx="6.5" cy="6.5" r="2" fill="none" stroke="#1b1b1b" stroke-width="1.2"/>
          <path d="M8.5 6.5v1a1.3 1.3 0 0 0 2.3 0V6.5a4.3 4.3 0 1 0-1.6 3.3" fill="none" stroke="#1b1b1b" stroke-width="1.1"/>
        </svg>
        CORINNE@VARNOGEMS.COM.AU
      </li>
      <li class="contacts__item">
        <svg class="contacts__icon" viewBox="0 0 13 13" aria-hidden="true">
          <path d="M4 2.5l1.6 2.2-.9 1a5 5 0 0 0 2.6 2.6l1-.9 2.2 1.6-.8 1.5C6.5 10.4 2.6 6.5 2.5 3.3z" fill="#1b1b1b"/>
        </svg>
        +61 427 806 193
      </li>
      <li class="contacts__item">
        <svg class="contacts__icon" viewBox="0 0 13 13" aria-hidden="true">
          <circle cx="6.5" cy="6.5" r="4" fill="none" stroke="#1b1b1b" stroke-width="1"/>
          <ellipse cx="6.5" cy="6.5" rx="1.7" ry="4" fill="none" stroke="#1b1b1b" stroke-width="0.9"/>
          <path d="M2.5 6.5h8" stroke="#1b1b1b" stroke-width="0.9"/>
        </svg>
        PERTH AUSTRALIA
      </li>
    </ul>
  </section>

</main>
</body>
</html>
```